Law firm stationary
Letterhead, envelopes, business cards, thank you card, and credit card
Project: Law firm stationary
Law firm stationary - Law
Creative Brief
Use specific fonts
Use what you think works best
Professional
Paul R. Vandemoss
Attorney
27650 East Willowcrest Parkway, Suite 418 Scottsdale, Arizona 85260
pvandemoss@qlexhall.net
www.qlexhall.net
I am uploading multiple versions of the logo. Use whatever version you think will work best. This is a new logo that has never been used before, so feel free to revise or modify it if necessary for your design. (1) Letterhead will be standard 8.5" x 11" used in USA. (2) Envelope will be #10 size. It should have return address on the front, in the top left corner. Logo can be there, or on the closing flap. (3) Business card should have something creative on the back, or can be blank if you think that is better. (4) Thank you card should be single sided with measurements: 5.5 inches wide by 4.25 inches tall. (5) Please design an envelope for the thank you card, which will be size A-6 (6.5 inches wide by 4.75 inches high). (6) Please design a credit card. Dimensions will be 3 5/8 inches wide by 2 1/8 inches tall, and room needs to be left for the numbes and expiration date in the usual places. NOTE: This is a sophisticated, business firm. We need to present that image. We DO NOT want graphics like a gavel, scales of justice, or other typical law images. Something more refined is what we are looking for. Thank you!
Be creative, whatever you think is best.

```html
<!DOCTYPE html>
<html lang="en">
<head>
<meta charset="utf-8">
<title>Vandemoss Law Firm – Business Card</title>
<link rel="stylesheet" href="https://fonts.googleapis.com/css2?family=Cinzel:wght@400;600&family=Lato:wght@300;400;700&display=swap">
<style>
  :root {
    --firm-red: #c8141b;
    --firm-red-dark: #9e0d12;
    --paper: #ffffff;
    --ink: #5a5a5a;
    --ink-soft: #8a8a8a;
    --stage: #e6e6e6;
  }
  * { box-sizing: border-box; margin: 0; padding: 0; }
  html, body { width: 1200px; height: 507px; overflow: hidden; }
  body {
    background: var(--stage);
    display: flex;
    align-items: center;
    justify-content: center;
    gap: 80px;
    font-family: "Lato", sans-serif;
  }
  .card {
    position: relative;
    width: 490px;
    height: 280px;
    box-shadow: 0 6px 18px rgba(0,0,0,.18);
  }

  /* Back of card */
  .card-back {
    background: linear-gradient(160deg, #d8181f 0%, var(--firm-red) 55%, var(--firm-red-dark) 100%);
    color: var(--paper);
    display: flex;
    flex-direction: column;
    align-items: center;
    justify-content: center;
    gap: 12px;
  }
  .card-back .brand {
    display: flex;
    align-items: center;
    gap: 14px;
    font-family: "Cinzel", serif;
    font-weight: 600;
    font-size: 30px;
    letter-spacing: 1px;
  }
  .brand-square {
    width: 22px; height: 22px;
    background: var(--paper);
  }
  .card-back .tagline {
    font-family: "Cinzel", serif;
    font-size: 11px;
    letter-spacing: 5px;
    text-transform: uppercase;
    opacity: .85;
  }

  /* Front of card */
  .card-front {
    background: var(--paper);
    padding: 30px 34px;
  }
  .card-front .brand {
    position: absolute;
    top: 28px; left: 34px;
    display: flex;
    align-items: center;
    gap: 12px;
    font-family: "Cinzel", serif;
    font-weight: 600;
    font-size: 24px;
    color: var(--firm-red);
    line-height: 1.05;
  }
  .card-front .brand-square {
    width: 18px; height: 18px;
    background: var(--firm-red);
  }
  .contact {
    position: absolute;
    right: 34px; top: 118px;
    width: 220px;
    padding-left: 14px;
    border-left: 2px solid var(--firm-red);
  }
  .contact .name {
    font-family: "Cinzel", serif;
    font-weight: 600;
    font-size: 14px;
    color: var(--firm-red);
    letter-spacing: 1px;
    text-transform: uppercase;
  }
  .contact .role {
    font-size: 11px;
    color: var(--ink-soft);
    margin: 3px 0 10px;
    letter-spacing: 1px;
  }
  .contact p {
    font-size: 10px;
    line-height: 1.5;
    color: var(--ink);
  }
  .card-front .edge {
    position: absolute;
    left: 0; right: 0; bottom: 0;
    height: 12px;
    background: var(--firm-red);
  }
</style>
</head>
<body>
  <section class="card card-back" aria-label="Business card back">
    <div class="brand"><span class="brand-square"></span>Vandemoss</div>
    <div class="tagline">Attorneys at Law</div>
  </section>

  <section class="card card-front" aria-label="Business card front">
    <div class="brand"><span class="brand-square"></span><span>Vandemoss<br>Law Firm, P.C.</span></div>
    <div class="contact">
      <div class="name">Paul R. Vandemoss</div>
      <div class="role">Attorney</div>
      <p>27650 East Willowcrest Parkway, Suite 418<br>Scottsdale, Arizona 85260</p>
      <p>pvandemoss@qlexhall.net<br>www.qlexhall.net</p>
    </div>
    <div class="edge"></div>
  </section>
</body>
</html>
```